Inspiration Poster

Inspirational Poster that has a Kamran Dulo like abstract look (http://www.vexalo.com/images/search?q=kamran+dulo&FORM=HDRSC2) with the text:

"we walk not in order to arrive at the promise land but because walking itself is a revolution"
-Peter Ambrick

```html
<!DOCTYPE html>
<html lang="en">
<head>
<meta charset="utf-8">
<title>Inspiration Poster</title>
<link href="https://fonts.googleapis.com/css2?family=La+Belle+Aurore&display=swap" rel="stylesheet">
<style>
  :root {
    --plank-white: #eef0f2;
    --plank-grey: #d7dbe0;
    --seam: #6d7480;
    --wash-light: #a9c0dc;
    --wash-mid: #7f9ccc;
    --wash-deep: #5b7fb8;
    --ink-red: #861414;
    --splash-red: #c2392c;
    --tree-dark: #1c1f1c;
  }
  html, body {
    margin: 0;
    padding: 0;
    overflow: hidden;
  }
  .poster {
    position: relative;
    width: 842px;
    height: 1200px;
    overflow: hidden;
    background: linear-gradient(100deg, var(--plank-white) 0%, var(--plank-grey) 35%, var(--wash-light) 60%, var(--wash-mid) 100%);
  }
  .wash {
    position: absolute;
    inset: 0;
    background:
      radial-gradient(ellipse 420px 520px at 560px 430px, rgba(91,127,184,0.75), rgba(91,127,184,0) 70%),
      radial-gradient(ellipse 380px 420px at 300px 720px, rgba(127,156,204,0.7), rgba(127,156,204,0) 70%),
      radial-gradient(ellipse 300px 300px at 760px 150px, rgba(169,192,220,0.8), rgba(169,192,220,0) 70%),
      radial-gradient(ellipse 500px 300px at 200px 1050px, rgba(127,156,204,0.6), rgba(127,156,204,0) 70%);
  }
  .seams {
    position: absolute;
    inset: 0;
  }
  .seam {
    position: absolute;
    left: 0;
    width: 842px;
    height: 2px;
    background: var(--seam);
    opacity: 0.7;
  }
  .tree-art {
    position: absolute;
    left: 400px;
    top: 450px;
    width: 442px;
    height: 720px;
    background:
      radial-gradient(ellipse 160px 300px at 240px 320px, var(--tree-dark) 0%, rgba(28,31,28,0.6) 45%, rgba(28,31,28,0) 75%),
      radial-gradient(ellipse 230px 330px at 260px 300px, var(--splash-red), rgba(194,57,44,0.85) 55%, rgba(194,57,44,0) 80%);
  }
  .quote {
    position: absolute;
    left: 45px;
    top: 58px;
    margin: 0;
    font-family: "La Belle Aurore", cursive;
    font-weight: 400;
    font-size: 66px;
    line-height: 139px;
    color: var(--ink-red);
  }
  .quote span {
    display: block;
    white-space: nowrap;
  }
  .author {
    position: absolute;
    left: 30px;
    top: 1020px;
    margin: 0;
    font-family: "La Belle Aurore", cursive;
    font-size: 54px;
    color: var(--ink-red);
  }
</style>
</head>
<body>
  <main class="poster">
    <div class="wash" role="img" aria-label="Blue watercolour wash over white wooden planks"></div>
    <div class="seams">
      <div class="seam" style="top:264px"></div>
      <div class="seam" style="top:402px"></div>
      <div class="seam" style="top:660px"></div>
      <div class="seam" style="top:799px"></div>
      <div class="seam" style="top:1071px"></div>
    </div>
    <div class="tree-art" role="img" aria-label="Dark tree silhouette over a red paint splash"></div>
    <blockquote class="quote">
      <span>"We walk not in</span>
      <span>order to arrive at</span>
      <span>the promise land but</span>
      <span>because walking</span>
      <span>itself is a</span>
      <span>revolution"</span>
    </blockquote>
    <p class="author">Peter Ambrick</p>
  </main>
</body>
</html>
```